Business Card Professional Clean - Ledgerpeak

Create a business card for my company that deals with Cryptocurrencies. I have a few designs ideas that I'd like to be implemented. Thanks! I will include the logo files, and a link to the design styles that I like.

Target Market(s)

Professionals

Industry/Entity Type

Consulting

Contact Information for Business Card

Name: Mark Dunn
Title: CEO/Technical Director
Phone: (587)430-9158
E-mail: mdunn@ledgerpeak.example
Address: Suite 512, 208-3375 Harwood Lane NW

Twitter: @LedgerPeakYYC
Instagram: ledgerpeakyyc

Colors
92b5d7
3276b5
33a6d7
85acd3
85cae6
0592cd

Requirements
Must have
• Some colors that match with the logo and the pictures I put in below.
• Ideally the finished product would look something like the attachments showing the color gradient I want.
Nice to have
• Please see some of the attachments I've included. This is very close to the final product that I would like to see. If someone could recreate something like those I would definitely feel pretty good about it.
• For the instagram and twitter please use the symbols/icon to represent it on the card.
Should not have
• No crazy colors and unprofessional styles. I just want clear info. Don't go outside the boundaries of the colors in the attachment and we should be good. No crazy weird fonts either.

```html
<!DOCTYPE html>
<html lang="en">
<head>
<meta charset="utf-8">
<title>Ledgerpeak Business Card</title>
<link rel="stylesheet" href="https://fonts.googleapis.com/css2?family=Tenor+Sans&family=Arimo&display=swap">
<style>
  :root {
    --paper: #ffffff;
    --ink-black: #090606;
    --band-teal: #0598bd;
    --band-blue: #0a6aa0;
    --accent-light: #1ea3c8;
    --banner: #62a8c4;
    --brand-navy: #0c4f8a;
    --title-dark: #1a3550;
    --contact-text: #ffffff;
  }
  * { margin: 0; padding: 0; box-sizing: border-box; }
  html, body {
    width: 941px; height: 1200px; overflow: hidden;
    background: var(--paper);
  }
  .sheet {
    position: relative;
    width: 595px; height: 758px;
    transform: scale(1.5815);
    transform-origin: 0 0;
  }
  .card {
    position: absolute;
    left: 33px; width: 527px; height: 318px;
    border-radius: 22px;
    overflow: hidden;
    background: var(--ink-black);
  }
  .card--front { top: 38px; }
  .card--back { top: 406px; height: 317px; }

  .band { position: absolute; left: 0; width: 100%; }
  .band--top { top: 0; height: 40px; background: var(--band-teal); }
  .band--bottom { bottom: 0; height: 40px; background: var(--band-blue); }
  .band--contact { bottom: 0; height: 116px; background: var(--band-blue); }

  .side-accent { position: absolute; left: 0; top: 92px; width: 100px; height: 132px; }

  .brand-name {
    position: absolute;
    font-family: "Tenor Sans", sans-serif;
    color: var(--brand-navy);
    letter-spacing: 1px;
    white-space: nowrap;
  }
  .brand-name--front { left: 150px; top: 138px; font-size: 44px; }
  .brand-name--corner { right: 16px; top: 54px; font-size: 10px; letter-spacing: .5px; }

  .name-banner { position: absolute; left: 30px; top: 101px; width: 497px; height: 68px; }
  .holder {
    position: absolute; left: 147px; top: 100px;
    font-family: "Tenor Sans", sans-serif;
  }
  .holder__name {
    font-size: 37px; line-height: 42px; color: var(--brand-navy);
    letter-spacing: 1px; margin-left: 10px;
  }
  .holder__title { font-size: 18px; line-height: 22px; color: var(--title-dark); }
  .holder__title .role { color: var(--brand-navy); }

  .contact {
    position: absolute;
    font-family: "Arimo", Arial, sans-serif;
    font-size: 12.5px;
    color: var(--contact-text);
    display: flex; align-items: center; gap: 7px;
    white-space: nowrap;
  }
  .contact svg { width: 13px; height: 13px; flex: none; }
  .contact .at { font-size: 15px; font-weight: bold; width: 13px; text-align: center; }
  .contact--phone { left: 30px; top: 226px; }
  .contact--email { left: 30px; top: 251px; }
  .contact--address { left: 30px; top: 277px; }
  .contact--social { right: 24px; }
  .contact--twitter { top: 252px; }
  .contact--instagram { top: 277px; }
  .social-mark {
    width: 12px; height: 12px; border: 1.4px solid var(--contact-text); border-radius: 2px;
  }
</style>
</head>
<body>
<main class="sheet">

  <section class="card card--front" aria-label="Card front">
    <div class="band band--top"></div>
    <div class="band band--bottom"></div>
    <svg class="side-accent" viewBox="0 0 100 132" aria-hidden="true">
      <polygon points="0,0 97,0 40,66 97,132 0,132" fill="var(--accent-light)"/>
      <polygon points="0,80 42,68 97,132 0,132" fill="var(--band-blue)"/>
    </svg>
    <div class="brand-name brand-name--front">Ledgerpeak</div>
  </section>

  <section class="card card--back" aria-label="Card back">
    <div class="band band--contact"></div>
    <div class="brand-name brand-name--corner">Ledgerpeak</div>

    <svg class="name-banner" viewBox="0 0 497 68" aria-hidden="true">
      <polygon points="0,34 36,0 497,0 497,68 36,68" fill="var(--banner)"/>
    </svg>
    <div class="holder">
      <div class="holder__name">MARK DUNN</div>
      <div class="holder__title"><span class="role">CEO/Technical</span> Director</div>
    </div>

    <div class="contact contact--phone">
      <svg viewBox="0 0 24 24" aria-hidden="true"><path d="M6.6 2.5l3 3.5-2 2.2c1 2.6 3.2 5 6 6.3l2.2-2 3.6 3-2.2 3.6C10 19 4.7 13.4 3.6 5.2z" fill="none" stroke="#fff" stroke-width="1.8" stroke-linejoin="round"/></svg>
      <span>(587)430-9158</span>
    </div>
    <div class="contact contact--email">
      <span class="at">@</span>
      <span>mdunn@ledgerpeak.example</span>
    </div>
    <div class="contact contact--address">
      <svg viewBox="0 0 24 24" aria-hidden="true"><path d="M2 12L12 3l10 9M5 10v11h5v-6h4v6h5V10" fill="none" stroke="#fff" stroke-width="2" stroke-linejoin="round"/></svg>
      <span>Suite 512, 208-3375 Harwood Lane NW</span>
    </div>

    <div class="contact contact--social contact--twitter">
      <span>@LedgerPeakYYC</span><span class="social-mark"></span>
    </div>
    <div class="contact contact--social contact--instagram">
      <span>@ledgerpeakyyc</span><span class="social-mark"></span>
    </div>
  </section>

</main>
</body>
</html>
```